High-End Print/Digital Ad for Unique Luxury Travel Company Required

Objective:
Design a compelling and visually striking advertisement that highlights our company’s unmatched luxury travel experiences. The ad should elevate our brand image, spark curiosity, and drive prospective clients to contact us.
Target Audience:
• Affluent individuals seeking extraordinary, tailor-made travel experiences
• Affluent, luxury, high-net-worth individuals looking for value, expertise, and white-glove service
• Professionals or retirees who appreciate unique, thoughtfully curated travel over mainstream tourism
Key Messages to Communicate:
• One-of-a-kind luxury travel: Once-in-a-lifetime experiences that are curated with creativity and meticulous attention to detail
• Exceptional service: White-glove, personalized planning from start to finish
• 38 years’ travel experience – expert knowledge of destinations, modes of travel, premium accommodations and well-established, meaningful industry connections.
• Highly trusted: Cruise line executives often say, “No one does what you do.”
Tone and Style:
• Elegant, luxurious, sophisticated
• Eye-catching, polished, and modern
• Professional but warm—conveys trust and credibility
• High-impact visuals (full-bleed imagery, custom graphics, or high-end photography)
Deliverables:
• One full-page print ad and digital ad
• Ready-to-print, high-resolution file + working file (PSD, AI, etc.)
Optional: Social media-optimized version or short motion-graphic variation (if designer offers it)
Inspiration & Visual Style Suggestions:
• Think Velvet Voyager, Brimley Hart Wanderer, Seven Lanterns, or Oriel Retreats ad styles
• Large, emotive imagery with elegant typography
• Clean layout that speaks luxury, clarity, and trust
Copy Direction (draft):
For those who’ve explored the world—and crave something beyond the ordinary.
Each journey is a masterfully curated experience, rich in detail, seamless in execution, and unforgettable in every way.
Founded in 1997, Tidewell Journeys is a unique travel company specializing in cruising, all-inclusive luxury properties, and tours world-wide for individuals, groups, and incentives.
We offer an exceptional range of services designed to ensure every journey is flawlessly executed and truly unforgettable.
Let us help you plan your next extraordinary adventure.
Note: You may refine the copy slightly based on layout or format needs.
Other Resources for References:
1. Website - www.tidewelljourneys.example

```html
<!DOCTYPE html>
<html lang="en">
<head>
<meta charset="utf-8">
<title>Tidewell Journeys — Trips of a Lifetime</title>
<link rel="stylesheet" href="https://fonts.googleapis.com/css2?family=Arimo:wght@400&family=Bodoni+Moda:opsz,wght@96,400&family=Cinzel:wght@400;500&family=EB+Garamond:wght@400;600&display=swap">
<style>
  :root {
    --navy: #24358a;
    --ink: #2b2b2b;
    --shadow: #1e1e22;
    --white: #ffffff;
    --ice-deep: #0d3f5c;
    --ice-mid: #1f7fa6;
    --ice-light: #8fd3e6;
    --rule: #9aa3c0;
  }
  * { margin: 0; padding: 0; box-sizing: border-box; }
  html, body { width: 849px; height: 1200px; overflow: hidden; background: var(--white); }
  .ad { position: relative; width: 849px; height: 1200px; overflow: hidden; background: var(--white); }

  .photo { position: absolute; }
  .photo--hero {
    left: 0; top: 0; width: 849px; height: 651px;
    background:
      radial-gradient(ellipse 30% 28% at 70% 62%, #e8f7fb 0%, #b6e5f0 40%, transparent 75%),
      radial-gradient(ellipse 60% 30% at 30% 95%, #0a1a22 0%, transparent 70%),
      linear-gradient(160deg, var(--ice-deep) 0%, var(--ice-mid) 45%, var(--ice-light) 70%, var(--ice-mid) 100%);
  }
  .photo--ship {
    left: 495px; top: 567px; width: 354px; height: 195px;
    background: linear-gradient(180deg, #5f6fa8 0%, #a9b3d6 40%, #e9e3de 62%, #7b89b8 78%, #3f5288 100%);
  }
  .photo--heather {
    left: 0; top: 920px; width: 345px; height: 121px;
    background: linear-gradient(160deg, #f08a3a 0%, #7a4f7a 28%, #a74c9a 55%, #2f5fb0 72%, #6f8a3a 100%);
  }
  .photo--resort {
    left: 352px; top: 920px; width: 183px; height: 121px;
    background: linear-gradient(180deg, #dfe9ef 0%, #6f8f7a 35%, #2f6b3c 60%, #2fb8d6 85%, #45c6dd 100%);
  }
  .photo--sunset {
    left: 790px; top: 943px; width: 59px; height: 257px;
    background: linear-gradient(180deg, #a8cde0 0%, #d3c6cf 45%, #f2a98f 70%, #e58aa0 85%, #b6c5dc 100%);
  }

  .headline { position: absolute; left: 0; top: 0; width: 849px; height: 651px; color: var(--white); font-weight: 400; }
  .headline__kicker {
    position: absolute; left: 76px; top: 40px;
    font-family: "Arimo", Arial, sans-serif; font-size: 80px; line-height: 1;
    letter-spacing: -3px; text-shadow: 4px 4px 0 var(--shadow);
  }
  .headline__word { position: absolute; left: 0; width: 849px; height: 262px;
    font-family: "Bodoni Moda", "Didot", serif; font-size: 262px; line-height: 262px; }
  .headline__word--life { top: 114px; }
  .headline__word--time { top: 313px; }
  .headline__letter { position: absolute; top: 0; text-shadow: 5px 5px 0 var(--shadow); }

  .intro { position: absolute; left: 88px; top: 712px; width: 372px; }
  .intro__title {
    font-family: "Cinzel", serif; font-weight: 400; font-size: 15.5px; line-height: 17px;
    color: var(--navy); letter-spacing: -0.2px; margin-bottom: 14px;
  }
  .intro__text {
    font-family: "Arimo", Arial, sans-serif; font-size: 10.8px; line-height: 14px;
    color: var(--ink); margin-bottom: 13px;
  }

  .pillars { position: absolute; left: 563px; top: 785px; width: 214px; list-style: none; }
  .pillar { margin-bottom: 10px; }
  .pillar__title {
    font-family: "Cinzel", serif; font-weight: 400; font-size: 13.5px; line-height: 15px;
    color: var(--navy); letter-spacing: -0.3px;
  }
  .pillar__text { font-family: "Arimo", Arial, sans-serif; font-size: 10.8px; line-height: 13.6px; color: var(--ink); }

  .brand {
    position: absolute; left: 292px; top: 1080px; width: 230px; height: 30px;
    display: flex; align-items: center; justify-content: center; gap: 7px;
    font-family: "Cinzel", serif; font-size: 21px; color: var(--navy); letter-spacing: -0.3px;
  }
  .brand__dot { width: 14px; height: 14px; border-radius: 50%; background: var(--navy); }

  .contact { position: absolute; top: 1120px; font-family: "EB Garamond", Garamond, serif; font-size: 13px; line-height: 18.5px; color: var(--ink); }
  .contact strong { font-weight: 600; }
  .contact--phone { left: 80px; }
  .contact--phone .contact__line { padding-left: 20px; position: relative; }
  .contact--web { left: 571px; }
  .contact--web .contact__line { padding-left: 21px; position: relative; }
  .contact__icon { position: absolute; left: 0; top: 3px; width: 13px; height: 13px; }
  .tagline {
    position: absolute; left: 280px; top: 1120px; width: 240px; text-align: center;
    font-family: "EB Garamond", Garamond, serif; font-weight: 600; font-size: 13.5px; line-height: 18px; color: var(--ink);
  }
  .divider { position: absolute; top: 1122px; width: 1px; height: 31px; background: var(--rule); }
  .divider--left { left: 246px; }
  .divider--right { left: 553px; }
</style>
</head>
<body>
<main class="ad">
  <div class="photo photo--hero" role="img" aria-label="Explorer in a red helmet walking through a glowing blue glacier ice cave"></div>

  <h1 class="headline" aria-label="trips of a lifetime">
    <span class="headline__kicker">trips of a</span>
    <span class="headline__word headline__word--life">
      <span class="headline__letter" style="left:78px">L</span>
      <span class="headline__letter" style="left:240px">I</span>
      <span class="headline__letter" style="left:338px">F</span>
      <span class="headline__letter" style="left:490px">E</span>
    </span>
    <span class="headline__word headline__word--time">
      <span class="headline__letter" style="left:78px">T</span>
      <span class="headline__letter" style="left:228px">I</span>
      <span class="headline__letter" style="left:290px">M</span>
      <span class="headline__letter" style="left:490px">E</span>
    </span>
  </h1>

  <div class="photo photo--ship" role="img" aria-label="Large luxury cruise ship at sea under a dramatic cloudy sky"></div>

  <section class="intro">
    <h2 class="intro__title">For those who’ve explored the world and crave something beyond the ordinary.</h2>
    <p class="intro__text">Each journey is a masterfully curated experience, rich in detail, seamless in execution, and unforgettable in every way.</p>
    <p class="intro__text">Founded in 1997, Tidewell Journeys is a unique travel company specializing in cruising, all-inclusive luxury properties, and tours world-wide for individuals, groups, and incentives.</p>
    <p class="intro__text">We offer an exceptional range of services designed to ensure every journey is flawlessly executed and truly unforgettable.</p>
  </section>

  <ul class="pillars">
    <li class="pillar">
      <h3 class="pillar__title">One-of-a-kind luxury travel</h3>
      <p class="pillar__text">Once-in-a-lifetime experiences that are curated with creativity and meticulous attention to detail</p>
    </li>
    <li class="pillar">
      <h3 class="pillar__title">Exceptional service</h3>
      <p class="pillar__text">White-glove, personalized planning from start to finish</p>
    </li>
    <li class="pillar">
      <h3 class="pillar__title">38 years’ travel experience</h3>
      <p class="pillar__text">Expert knowledge of destinations, modes of travel, premium accommodations and well-established, meaningful industry connections.</p>
    </li>
    <li class="pillar">
      <h3 class="pillar__title">Highly trusted</h3>
      <p class="pillar__text">Cruise line executives often say, “No one does what you do.”</p>
    </li>
  </ul>

  <div class="photo photo--heather" role="img" aria-label="Purple heather hillside above a winding river at sunset"></div>
  <div class="photo photo--resort" role="img" aria-label="Tropical resort pool with thatched villas and palm trees"></div>
  <div class="photo photo--sunset" role="img" aria-label="Pastel sunset over the sea"></div>

  <div class="brand"><span class="brand__dot"></span><span class="brand__name">Tidewell Journeys</span></div>

  <div class="contact contact--phone">
    <p class="contact__line">
      <svg class="contact__icon" viewBox="0 0 24 24" aria-hidden="true"><path fill="#24358a" d="M6.6 10.8a15.1 15.1 0 0 0 6.6 6.6l2.2-2.2a1 1 0 0 1 1-.25 11.4 11.4 0 0 0 3.6.57 1 1 0 0 1 1 1V20a1 1 0 0 1-1 1A17 17 0 0 1 3 4a1 1 0 0 1 1-1h3.5a1 1 0 0 1 1 1c0 1.25.2 2.45.57 3.57a1 1 0 0 1-.25 1z"/></svg>
      <strong>toll-free:</strong> 877.555.0148
    </p>
    <p class="contact__line"><strong>p:</strong> 816.555.0172</p>
  </div>
  <span class="divider divider--left"></span>
  <p class="tagline">Let us help you<br>plan your next extraordinary adventure.</p>
  <span class="divider divider--right"></span>
  <div class="contact contact--web">
    <p class="contact__line">
      <svg class="contact__icon" viewBox="0 0 24 24" aria-hidden="true"><rect x="2.5" y="5" width="19" height="14" rx="1.5" fill="none" stroke="#24358a" stroke-width="1.8"/><path d="M3 6l9 7 9-7" fill="none" stroke="#24358a" stroke-width="1.8"/></svg>
      travelplans@tidewelljourneys.example
    </p>
    <p class="contact__line">
      <svg class="contact__icon" viewBox="0 0 24 24" aria-hidden="true"><g fill="none" stroke="#24358a" stroke-width="1.8"><circle cx="12" cy="12" r="9.5"/><ellipse cx="12" cy="12" rx="4" ry="9.5"/><path d="M2.5 12h19"/></g></svg>
      tidewelljourneys.example
    </p>
  </div>
</main>
</body>
</html>
```